Internet and T.V. Services

We will need a two page brochure highlighting the services of satelitte t.v. and internet for our sales team. We are a camp and catering company focused on remote locations in northern Canada that would like to offer a first class t.v. and internet services to the camps that we provide catering to.

Target Market(s)

Adults based in western speaking countries aged 25-35 business professionals.

Industry/Entity Type

Internet

Font styles to use
Serif

Colors

Designer to choose colors to be used in the design.

Requirements
Must have
• -Company logo
-Two pages (4 sides)
-An emotional connection between family life and remote camp life
-Break down of services for t.v. and internet
-Pictures in background representing the above
-emphasis that it is an upsell for our company
Nice to have
• -company logo to look like a globe with an airplane flying around it (latitude and longitude lines)

```html
<!DOCTYPE html>
<html lang="en">
<head>
<meta charset="utf-8">
<title>Satellite T.V. and Internet Services</title>
<link href="https://fonts.googleapis.com/css2?family=Tinos:ital,wght@0,400;0,700;1,400&display=swap" rel="stylesheet">
<style>
:root{
  --paper:#ffffff;
  --band:#fcc435;
  --blue:#1f63ab;
  --navy:#1d4d8c;
  --red:#b8323a;
  --ink:#2b2b2b;
  --panel:#b9dcea;
  --mark:#222222;
}
*{margin:0;padding:0;box-sizing:border-box}
html,body{width:1200px;height:755px;overflow:hidden;background:var(--paper)}
body{font-family:"Tinos","Times New Roman",serif;color:var(--ink);position:relative}
.abs{position:absolute}
.header-band{height:41px;background:var(--band);display:flex;align-items:center;justify-content:center;
  color:var(--blue);font-weight:700;font-size:18px;letter-spacing:.3px}
.left-band{left:24px;top:60px;width:487px}
.right-band{left:687px;top:60px;width:489px}
.lead{left:74px;top:123px;width:480px;color:var(--red);font-weight:700;font-size:16.5px;line-height:21px}
.plan-panel{left:74px;top:168px;width:476px;height:142px;background:var(--panel);padding:6px}
.plan-inner{width:100%;height:100%;border:1px dotted var(--navy);display:flex;padding:12px 0 0 23px;font-size:13px;line-height:16.5px}
.plan-col{width:252px}
.plan-col h3{color:var(--navy);font-size:13px;font-weight:700;margin-bottom:8px}
.plan-col .or{color:var(--red);font-size:9px;line-height:14px}
.terms{left:74px;top:325px;width:476px;text-align:center;color:var(--blue);font-weight:700;font-size:13.5px;line-height:17.5px}
.photo-dishes{left:74px;top:388px;width:476px;height:181px;background:linear-gradient(180deg,#a9b8b8 0%,#7d8f6a 40%,#4f6a3a 100%)}
.upgrade-icon{left:150px;top:588px}
.upgrade{left:232px;top:592px;font-size:20px}
.upgrade b{color:var(--red);font-weight:700}
.note{left:74px;top:630px;width:480px;font-style:italic;font-size:12.5px;line-height:18px}
.photo-reader{left:619px;top:111px;width:506px;height:338px;background:linear-gradient(160deg,#d9d6cc 0%,#c9b8a2 45%,#b07a56 100%)}
.tagline{left:619px;top:454px;width:520px;color:var(--blue);font-weight:700;font-size:13.5px;line-height:18px}
.service-head{color:var(--red);font-weight:700;font-size:12.5px;font-variant:small-caps;font-size:13px}
.service-list{list-style:none;font-size:13px;line-height:21.5px}
.service-list li::before{content:"❖";color:var(--red);margin-right:4px}
.office{left:619px;top:506px}
.camp{left:619px;top:583px}
.slug{font-family:Arial,sans-serif;font-size:7px;color:var(--mark)}
</style>
</head>
<body>

<svg class="abs" style="left:0;top:0" width="1200" height="755" aria-hidden="true">
  <g class="crop-marks" stroke="#000" stroke-width="0.6">
    <line x1="0" y1="24" x2="18" y2="24"/><line x1="24" y1="0" x2="24" y2="18"/>
    <line x1="1182" y1="24" x2="1200" y2="24"/><line x1="1176" y1="0" x2="1176" y2="18"/>
    <line x1="0" y1="730" x2="18" y2="730"/><line x1="24" y1="737" x2="24" y2="755"/>
    <line x1="1182" y1="730" x2="1200" y2="730"/><line x1="1176" y1="737" x2="1176" y2="755"/>
  </g>
  <g class="grey-scale">
    <rect x="40" y="11" width="14" height="14" fill="#000"/><rect x="54" y="11" width="14" height="14" fill="#1a1a1a"/>
    <rect x="68" y="11" width="14" height="14" fill="#333"/><rect x="82" y="11" width="14" height="14" fill="#4d4d4d"/>
    <rect x="96" y="11" width="14" height="14" fill="#666"/><rect x="110" y="11" width="14" height="14" fill="#808080"/>
    <rect x="124" y="11" width="14" height="14" fill="#999"/><rect x="138" y="11" width="14" height="14" fill="#b3b3b3"/>
    <rect x="152" y="11" width="14" height="14" fill="#ccc"/><rect x="166" y="11" width="14" height="14" fill="#e6e6e6"/>
    <rect x="180" y="11" width="14" height="14" fill="#fff" stroke="#000" stroke-width=".5"/>
  </g>
  <g class="colour-bar">
    <rect x="986" y="11" width="14" height="14" fill="#fff200"/><rect x="1000" y="11" width="14" height="14" fill="#ec008c"/>
    <rect x="1014" y="11" width="14" height="14" fill="#00aeef"/><rect x="1028" y="11" width="14" height="14" fill="#2e3192"/>
    <rect x="1042" y="11" width="14" height="14" fill="#00a651"/><rect x="1056" y="11" width="14" height="14" fill="#ed1c24"/>
    <rect x="1070" y="11" width="14" height="14" fill="#231f20"/><rect x="1084" y="11" width="14" height="14" fill="#fff799"/>
    <rect x="1098" y="11" width="14" height="14" fill="#f49ac1"/><rect x="1112" y="11" width="14" height="14" fill="#6dcff6"/>
    <rect x="1126" y="11" width="14" height="14" fill="#a3a3a3"/><rect x="1140" y="11" width="14" height="14" fill="#7a7a7a"/>
  </g>
  <g class="registration" fill="none" stroke="#000" stroke-width=".8">
    <circle cx="600" cy="18" r="5"/><line x1="592" y1="18" x2="608" y2="18"/><line x1="600" y1="10" x2="600" y2="26"/>
    <circle cx="18" cy="377" r="5"/><line x1="10" y1="377" x2="26" y2="377"/><line x1="18" y1="369" x2="18" y2="385"/>
    <circle cx="1182" cy="377" r="5"/><line x1="1174" y1="377" x2="1190" y2="377"/><line x1="1182" y1="369" x2="1182" y2="385"/>
    <circle cx="600" cy="737" r="5"/><line x1="592" y1="737" x2="608" y2="737"/><line x1="600" y1="729" x2="600" y2="745"/>
  </g>
  <rect x="35" y="723" width="1130" height="22" fill="none" stroke="#000" stroke-width=".4"/>
</svg>
<div class="abs slug" style="left:44px;top:732px">Brochure.indd 2</div>
<div class="abs slug" style="left:1110px;top:732px">4/11/14 4:28 AM</div>

<section class="page page-tv">
  <div class="abs header-band left-band">SATELLITE T.V.</div>
  <p class="abs lead">Is 16 channels good enough? Or do you want better? Why settle for less when you can get more?</p>

  <div class="abs plan-panel">
    <div class="plan-inner">
      <div class="plan-col">
        <h3>T.V. SHORT TERM</h3>
        <p>18 channel</p>
        <p>1 SD receiver (c/w 1 - ZFC per month)</p>
        <p class="or">OR</p>
        <p>36 channel</p>
        <p>1 HD receiver (c/w 1 - ZFC per month)</p>
      </div>
      <div class="plan-col">
        <h3>T.V. LONG TERM</h3>
        <p>48 channel</p>
        <p>Minimum - 1 year term</p>
        <p>1 HD receiver (c/w ZFC)</p>
        <p class="or">OR</p>
        <p>60 channels</p>
      </div>
    </div>
  </div>

  <div class="abs terms">
    <p>Minimum - 3 year term - due to licensing</p>
    <p>1 Electronic Programming Guide + 3 In House Channels</p>
    <p>2 - HD Receivers (both come with ZFC)</p>
  </div>

  <div class="abs photo-dishes" role="img" aria-label="Photo of two large satellite dishes on a green forested hillside"></div>

  <svg class="abs upgrade-icon" width="58" height="26" viewBox="0 0 58 26" aria-hidden="true">
    <rect x="1" y="4" width="9" height="20" fill="var(--red)"/>
    <path d="M12 6 H40 a3 3 0 0 1 0 6 H30 M12 6 V24 H34" fill="none" stroke="var(--red)" stroke-width="2.4" stroke-linejoin="round"/>
    <path d="M30 12 H54 M34 12 V17 M30 17 H36 M30 21 H35" fill="none" stroke="var(--red)" stroke-width="2.2" stroke-linecap="round"/>
  </svg>
  <p class="abs upgrade">Time for an <b>UPGRADE?</b></p>
  <p class="abs note">****Rig Camps will come with Fully Loaded Receivers including The Summit Channel as well as Free ZFC on the TV in the Recreation room.</p>
</section>

<section class="page page-internet">
  <div class="abs header-band right-band">INTERNET</div>
  <div class="abs photo-reader" role="img" aria-label="Photo of a smiling woman lying on a bed using a laptop beside an open book"></div>
  <p class="abs tagline">Are you feeling disconnected from the outside world? Our ‘better’ internet brings you into the moments you may miss while you’re away.</p>

  <div class="abs office">
    <h4 class="service-head">Satellite Internet - Office System</h4>
    <ul class="service-list">
      <li>Single Modem Internet Service (4 to 6 users) - Hardwire preferred</li>
      <li>VOIP phone line (Edmonton area code)</li>
    </ul>
  </div>
  <div class="abs camp">
    <h4 class="service-head">Camp/Dorm System</h4>
    <ul class="service-list">
      <li>Dual Modem Internet Service (20 to 30 users)</li>
      <li>PC Server controlled load sharing/cache interface</li>
      <li>Wireless Radios</li>
    </ul>
  </div>
</section>

</body>
</html>
```